Funeral Comparison Website Needs Designer For WireFrame Mock Up (That we've already done)

This should be a pretty quick design project. It's a single page based on a wireframe mockup we did.
Our site (restfulpathway.example) helps people find and compare funeral homes and cemeteries. Our site hasn't been redesigned since we launched in 2008, so it is fairly dated, and we've seen new competitors pop-up in the past year so we need to come up with a fresh redeisgn. We need someone to take our mockup and work their magic with it. As I mentioned this is a single page based on our wireframe mockup.
Please see attached mockup and logo.
Look and feel
Each slider illustrates characteristics of the customer's brand and the style your logo design should communicate.

```html
<!DOCTYPE html>
<html lang="en">
<head>
<meta charset="utf-8">
<title>Restful Pathway – Request Funeral Quotes</title>
<link href="https://fonts.googleapis.com/css2?family=Barlow+Semi+Condensed:wght@500;600&family=Barlow:wght@400;500;600&family=Open+Sans:wght@400;600&display=swap" rel="stylesheet">
<style>
:root{
  --green:#3f9e45;
  --green-bright:#4cb84a;
  --blue:#0d8fce;
  --blue-deep:#0a5a82;
  --blue-mid:#0a74aa;
  --blue-nav:#0e6e98;
  --grey-band:#d9dadc;
  --card:#f2f3f5;
  --ink:#1b1b1b;
  --footer:#1e1e1e;
  --footer-base:#141414;
  --footer-text:#5b5b5b;
  --footer-head:#9b9b9b;
  --white:#ffffff;
}
*{box-sizing:border-box;margin:0;padding:0}
html,body{width:852px;height:1200px;overflow:hidden}
body{position:relative;background:var(--white);font-family:"Barlow",sans-serif;color:var(--ink)}
.abs{position:absolute}

.call-bar{left:0;top:0;width:852px;height:21px;background:var(--green-bright);color:var(--white);font:600 12px "Barlow",sans-serif}
.call-bar .call{position:absolute;right:80px;top:3px}
.call-bar .dot{position:absolute;top:3px;width:15px;height:15px;border-radius:50%;background:var(--white)}

.hero{left:0;top:21px;width:852px;height:306px;background:radial-gradient(ellipse at 50% 20%,#f7f7f8 0%,#eceded 55%,#d7d8d9 100%)}
.brand{left:140px;top:62px;width:236px;display:flex;align-items:center;gap:7px;color:var(--blue-nav);font:600 18px "Barlow",sans-serif;white-space:nowrap}
.brand .mark{flex:none;width:14px;height:14px;border-radius:50%;background:var(--green)}
.nav{left:390px;top:58px;width:323px;display:flex;justify-content:space-between;font:400 9.5px "Barlow",sans-serif;color:#222}
.nav a{display:block;padding:6px 6px;color:inherit;text-decoration:none;text-transform:uppercase;white-space:nowrap}
.nav a.active{background:var(--blue-nav);color:var(--white);border-radius:2px;padding:6px 9px}

.hero-title{left:0;width:852px;top:116px;text-align:center;font:500 46px "Barlow Semi Condensed",sans-serif;color:var(--green);letter-spacing:-.5px}
.hero-sub{left:0;width:852px;top:168px;text-align:center;font:400 19px "Open Sans",sans-serif;color:#4a4a4a}

.choices{left:140px;top:205px;width:572px;height:133px;display:flex;box-shadow:0 4px 6px rgba(0,0,0,.25)}
.choice{display:flex;align-items:center;justify-content:center;text-align:center;color:var(--white);font:600 15px "Open Sans",sans-serif;line-height:19px;padding:0 14px}
.choice.blue{width:187px;background:linear-gradient(#05a3e0,#0a6f9f)}
.choice.green{width:198px;background:linear-gradient(#5fdc66,#45b349)}
.or{top:258px;width:36px;height:36px;border-radius:7px;background:var(--white);color:#222;font:600 11px "Open Sans",sans-serif;display:flex;align-items:center;justify-content:center;box-shadow:0 1px 3px rgba(0,0,0,.3)}

.testimonials{left:0;top:360px;width:852px;height:276px;background:var(--blue-deep)}
.notch-down{width:0;height:0;border-left:11px solid transparent;border-right:11px solid transparent}
.section-title{left:0;width:852px;text-align:center;font:600 30px "Barlow",sans-serif;letter-spacing:1px}
.testimonials .rule{left:140px;top:52px;width:572px;height:1px;background:#2a7aa3}
.quote{top:62px;width:183px;height:196px}
.quote .body{height:118px;background:var(--blue);color:var(--white);font:500 10.5px "Open Sans",sans-serif;line-height:14.5px;padding:16px 15px}
.quote .foot{height:78px;background:var(--blue-mid);position:relative}
.quote .foot::before{content:"";position:absolute;left:18px;top:0;border-left:10px solid transparent;border-right:10px solid transparent;border-top:10px solid var(--blue)}
.quote .name{position:absolute;left:12px;top:30px;color:var(--white);font:600 15px "Barlow",sans-serif;letter-spacing:1px}
.quote .city{position:absolute;left:12px;top:48px;color:var(--white);font:600 8.5px "Barlow",sans-serif}
.quote .photo{position:absolute;right:12px;top:11px;width:64px;height:64px;border-radius:50%;background:radial-gradient(circle at 50% 40%,#c9a28a 0%,#6f8db0 60%,#dfe3e7 100%)}
.slide-arrow{top:150px;width:26px;height:26px;border-radius:50%;background:var(--blue-mid)}

.ctas{left:140px;top:660px;width:572px;display:flex;gap:12px}
.cta{width:183px;height:51px;display:flex;align-items:center;justify-content:center;text-align:center;color:var(--white);font:600 15px "Barlow",sans-serif;line-height:18px;letter-spacing:.3px;text-transform:uppercase}
.cta.green{background:var(--green-bright);color:#10261a}
.cta.blue{background:var(--blue-deep)}
.cta.blue.tall{align-items:flex-start;padding-top:9px}

.support{left:0;top:731px;width:852px;height:278px;background:var(--grey-band)}
.support .rule{left:140px;top:57px;width:572px;height:1px;background:#5aa8c8}
.help{top:65px;width:183px;height:196px;background:var(--card);box-shadow:0 1px 3px rgba(0,0,0,.12);text-align:center}
.help h3{margin-top:7px;font:600 19px "Barlow",sans-serif;line-height:18px;color:var(--green);letter-spacing:.3px;text-transform:uppercase}
.help .big{font:500 42px "Barlow",sans-serif;color:var(--ink);margin-top:12px}
.help ul{list-style:none;position:absolute;left:14px;top:133px;text-align:left;font:400 11px "Open Sans",sans-serif;line-height:15px}
.help li::before{content:"→";font-size:8px;margin-right:12px}
.help .note{position:absolute;left:0;width:183px;top:133px;font:400 11px "Open Sans",sans-serif;line-height:15px}

.footer{left:0;top:1009px;width:852px;height:146px;background:var(--footer)}
.footer h4{font:600 11px "Open Sans",sans-serif;color:var(--footer-head);margin-bottom:8px}
.footer .col{top:19px}
.footer .links a{display:block;color:var(--footer-text);font:400 9.5px "Open Sans",sans-serif;line-height:18px;text-decoration:none}
.footer .contact p{color:var(--footer-text);font:400 11px "Open Sans",sans-serif;line-height:21.5px}
.footer .social p{display:flex;align-items:center;gap:22px;color:var(--footer-text);font:400 11px "Open Sans",sans-serif;height:29px}
.footer .social span.dot{width:17px;height:17px;border-radius:50%;background:#5f5f5f}
.base{left:0;top:1155px;width:852px;height:45px;background:var(--footer-base);color:#9a9a9a;font:400 7px "Open Sans",sans-serif}
.base p{position:absolute;left:141px;top:18px}
</style>
</head>
<body>

<div class="call-bar abs">
  <span class="call">Give us a call: 800 555 0199</span>
  <span class="dot" style="right:48px"></span>
  <span class="dot" style="right:29px"></span>
</div>

<div class="hero abs"></div>
<div class="brand abs"><span class="mark"></span>restfulpathway.example</div>
<nav class="nav abs">
  <a class="active" href="#">Home</a>
  <a href="#">How it works</a>
  <a href="#">About us</a>
  <a href="#">Contact us</a>
  <a href="#">Resources</a>
</nav>
<h1 class="hero-title abs">Request Funeral Quotes</h1>
<p class="hero-sub abs">Free No Obligations Price &amp; Services Quotes</p>

<div class="choices abs">
  <div class="choice blue">I am Planing For the Long Term Future</div>
  <div class="choice green">I Am Planing for a Death that will Occur Shortly</div>
  <div class="choice blue">A Death has just occured</div>
</div>
<div class="or abs" style="left:310px">OR</div>
<div class="or abs" style="left:510px">OR</div>

<section class="testimonials abs">
  <div class="notch-down abs" style="left:416px;top:0;border-top:10px solid var(--blue-mid)"></div>
  <h2 class="section-title abs" style="top:12px;color:var(--white)">TESTIMONIALS</h2>
  <div class="rule abs"></div>
  <div class="slide-arrow abs" style="left:108px"></div>
  <div class="slide-arrow abs" style="left:719px"></div>

  <article class="quote abs" style="left:140px">
    <p class="body">Lorem ipsum dolor sitaetscing elit. Aeneanmmodo ligula eget dolor. Aenemassa. Cum sociis natoque penatibus et m ridicu-lus mus. Donec quam feagnis dis parturiemontes, nascetulus mus. Donec quamfelis,</p>
    <div class="foot"><span class="name">Daniel</span><span class="city">Portland OR</span><div class="photo" role="img" aria-label="Portrait photo of the customer"></div></div>
  </article>
  <article class="quote abs" style="left:335px">
    <p class="body">Lorem ipsum dolor sitaetscing elit. Aeneanmmodo ligula eget dolor. Aenemassa. Cum sociis natoque penatibus et m ridicu-lus mus. Donec quam feagnis dis parturiemontes, nascetulus mus. Donec quamfelis,</p>
    <div class="foot"><span class="name">Daniel</span><span class="city">Portland OR</span><div class="photo" role="img" aria-label="Portrait photo of the customer"></div></div>
  </article>
  <article class="quote abs" style="left:530px">
    <p class="body">Lorem ipsum dolor sitaetscing elit. Aeneanmmodo ligula eget dolor. Aenemassa. Cum sociis natoque penatibus et m ridicu-lus mus. Donec quam feagnis dis parturiemontes, nascetulus mus. Donec quamfelis,</p>
    <div class="foot"><span class="name">Daniel</span><span class="city">Portland OR</span><div class="photo" role="img" aria-label="Portrait photo of the customer"></div></div>
  </article>
  <div class="notch-down abs" style="left:416px;top:276px;border-top:10px solid var(--blue-deep)"></div>
</section>

<div class="ctas abs">
  <a class="cta green">Get started<br>with pre-planning</a>
  <a class="cta blue">Get started</a>
  <a class="cta blue tall">Get started</a>
</div>

<section class="support abs">
  <div class="notch-down abs" style="left:416px;top:0;border-top:10px solid var(--white)"></div>
  <h2 class="section-title abs" style="top:18px;color:var(--ink)">SUPPORT CENTER</h2>
  <div class="rule abs"></div>

  <div class="help abs" style="left:140px">
    <h3>Questions &amp;<br>Answers</h3>
    <div class="big">Q&amp;A</div>
    <ul><li>How we help</li><li>How this works</li></ul>
  </div>
  <div class="help abs" style="left:335px">
    <h3>Resources</h3>
    <svg width="52" height="46" viewBox="0 0 52 46" style="margin-top:22px" aria-hidden="true">
      <path d="M8 24a18 18 0 0 1 31-12" fill="none" stroke="#111" stroke-width="7"/>
      <path d="M33 4l12 2-3 12z" fill="#111"/>
      <path d="M44 22a18 18 0 0 1-31 12" fill="none" stroke="#111" stroke-width="7"/>
      <path d="M19 42l-12-2 3-12z" fill="#111"/>
    </svg>
    <ul><li>Advice</li><li>Finances</li><li>Planning Guides</li></ul>
  </div>
  <div class="help abs" style="left:530px">
    <h3>Get more help</h3>
    <div class="big" style="font-size:58px;margin-top:6px">?</div>
    <p class="note">Learn about our Certified<br>consultant</p>
  </div>
</section>

<footer class="footer abs">
  <div class="col links abs" style="left:141px">
    <h4>Useful Links</h4>
    <a href="#">Home</a><a href="#">How It Works</a><a href="#">About Us</a><a href="#">Contact Us</a><a href="#">Resources</a>
  </div>
  <div class="col contact abs" style="left:355px">
    <h4>Contact Us</h4>
    <p>Tel: +44(0)20 7946 0321</p>
    <p>Mob: +44(0)75 0011 2468</p>
    <p>Email: support@restfulpathway.example</p>
  </div>
  <div class="col social abs" style="left:577px">
    <h4>Stay Connected</h4>
    <p><span class="dot"></span>Updates</p>
    <p><span class="dot"></span>Community</p>
  </div>
</footer>
<div class="base abs"><p>Copyright © 2013 Restful Pathway. All rights reserved. &nbsp;|&nbsp; Privacy Policy &nbsp;|&nbsp; Terms &amp; Conditions</p></div>

</body>
</html>
```